BRINDLEWAVE is a New Zealand based aerial imaging company performing mapping, surveying and videography

I would like a business card that is contemporary and clean. The font for the business name is called Gtec Technology and I would like to have the text "AERIAL IMAGING" under the "BRINDLEWAVE" name in a font similar to URW Gothic or another light modern font. Brindlewave performs aerial imaging projects using a hexacopter UAV. Surveying and mapping with 3D Digital Elevation Models are a focus, I also produce aerial photographs and video's including post editing.
Updates

Target Market(s)

Industrial plant managers, Property owners, Event organisers.

Industry/Entity Type

Videography

Contact Information for Business Card

BRINDLEWAVE AERIAL IMAGING. Owner Ross Pellow. Cell: 027 4913068. P.O. Box 8321 Dunedin, New Zealand.

Font styles to use
Other font styles liked:
• Gtec Technology

Colors
9bcb3b
33a6d7
ec1f27

Requirements
Must have
• Modern professional look.
Nice to have
• Perhaps an aerial image of a landscape who's location is not identifiable. Maybe use included image of my hexacopter on the back of the card? Not compulsory though.
Should not have
• Clip Art style images.

```html
<!DOCTYPE html>
<html lang="en">
<head>
<meta charset="utf-8">
<title>Brindlewave Aerial Imaging — Business Card</title>
<link href="https://fonts.googleapis.com/css2?family=Lato:wght@300;400;700&family=Michroma&display=swap" rel="stylesheet">
<style>
  :root {
    --backdrop: #e9e7e3;
    --card: #f7f7f7;
    --card-edge: #ffffff;
    --ink: #141414;
    --green: #5dbb3a;
    --red: #e8262d;
    --crease: rgba(0,0,0,0.10);
  }
  * { box-sizing: border-box; margin: 0; padding: 0; }
  html, body { width: 1200px; height: 800px; overflow: hidden; }
  body {
    background: var(--backdrop);
    font-family: "Lato", Arial, sans-serif;
    color: var(--ink);
    position: relative;
  }
  .card {
    position: absolute;
    width: 580px;
    height: 331px;
    background: linear-gradient(160deg, var(--card-edge), var(--card) 60%, #efefef);
    border-radius: 16px;
    box-shadow: 0 10px 24px rgba(0,0,0,0.18), 0 2px 4px rgba(0,0,0,0.10);
    overflow: hidden;
  }
  .card--front { left: 520px; top: 50px; }
  .card--back { left: 100px; top: 420px; }

  .wordmark { text-align: left; line-height: 1; }
  .wordmark__name {
    font-family: "Lato", Arial, sans-serif;
    font-weight: 700;
    font-size: 40px;
    letter-spacing: 1px;
    color: var(--green);
  }
  .wordmark__tagline {
    font-weight: 400;
    font-size: 25px;
    margin-top: 4px;
    margin-left: 40px;
    color: var(--ink);
  }

  .card--front .wordmark { position: absolute; left: 150px; top: 92px; }
  .front__swoosh { position: absolute; left: 0; top: 170px; width: 580px; height: 120px; }
  .front__caption {
    position: absolute;
    left: 0; right: 0; top: 252px;
    text-align: center;
    font-size: 15px;
    letter-spacing: 0.5px;
    color: var(--red);
  }

  .back__crease { position: absolute; left: 0; top: 0; width: 580px; height: 331px; }
  .card--back .wordmark { position: absolute; left: 30px; top: 108px; }
  .card--back .wordmark__name { font-size: 34px; }
  .card--back .wordmark__tagline { font-size: 22px; margin-left: 32px; }

  .contact { position: absolute; left: 330px; top: 78px; }
  .contact__name {
    font-family: "Michroma", Arial, sans-serif;
    font-size: 20px;
    color: var(--red);
    letter-spacing: 0.5px;
  }
  .contact__role {
    font-family: "Michroma", Arial, sans-serif;
    font-size: 13px;
    letter-spacing: 1px;
    margin-top: 2px;
  }
  .contact__list { list-style: none; margin-top: 28px; }
  .contact__item {
    display: flex;
    align-items: flex-start;
    gap: 14px;
    font-size: 15.5px;
    line-height: 1.25;
    margin-bottom: 5px;
  }
  .contact__icon { width: 16px; height: 16px; flex: none; margin-top: 1px; }
  .contact__item--address { margin-top: 8px; }
</style>
</head>
<body>

  <section class="card card--front" aria-label="Card front">
    <div class="wordmark">
      <div class="wordmark__name">BRINDLEWAVE</div>
      <div class="wordmark__tagline">Aerial Imaging</div>
    </div>
    <svg class="front__swoosh" viewBox="0 0 580 120" aria-hidden="true">
      <defs>
        <linearGradient id="swooshShade" x1="0" y1="0" x2="0" y2="1">
          <stop offset="0" stop-color="#000" stop-opacity="0.08"/>
          <stop offset="1" stop-color="#000" stop-opacity="0"/>
        </linearGradient>
      </defs>
      <path d="M40 20 Q290 -10 560 70 L560 110 Q290 40 40 40 Z" fill="url(#swooshShade)"/>
    </svg>
    <p class="front__caption">BRINDLEWAVE AERIAL IMAGING</p>
  </section>

  <section class="card card--back" aria-label="Card back">
    <svg class="back__crease" viewBox="0 0 580 331" aria-hidden="true">
      <defs>
        <linearGradient id="creaseShade" x1="0" y1="0" x2="1" y2="0">
          <stop offset="0" stop-color="#000" stop-opacity="0"/>
          <stop offset="1" stop-color="#000" stop-opacity="0.09"/>
        </linearGradient>
      </defs>
      <path d="M255 0 L300 0 L290 331 L245 331 Z" fill="url(#creaseShade)"/>
      <line x1="300" y1="0" x2="290" y2="331" stroke="var(--crease)" stroke-width="1"/>
    </svg>

    <div class="wordmark">
      <div class="wordmark__name">BRINDLEWAVE</div>
      <div class="wordmark__tagline">Aerial Imaging</div>
    </div>

    <div class="contact">
      <h1 class="contact__name">ROSS PELLOW</h1>
      <p class="contact__role">OWNER</p>
      <ul class="contact__list">
        <li class="contact__item">
          <svg class="contact__icon" viewBox="0 0 16 16" aria-hidden="true"><rect x="4" y="1" width="8" height="14" rx="1.5" fill="none" stroke="#e8262d" stroke-width="1.5"/><rect x="5.5" y="3" width="5" height="8" fill="#e8262d"/></svg>
          <span>027 4913068</span>
        </li>
        <li class="contact__item">
          <svg class="contact__icon" viewBox="0 0 16 16" aria-hidden="true"><rect x="1" y="3.5" width="14" height="9" fill="none" stroke="#e8262d" stroke-width="1.4"/><path d="M1 3.5 L8 9 L15 3.5" fill="none" stroke="#e8262d" stroke-width="1.4"/></svg>
          <span>info@yourmail.com</span>
        </li>
        <li class="contact__item">
          <svg class="contact__icon" viewBox="0 0 16 16" aria-hidden="true"><circle cx="8" cy="8" r="6.5" fill="none" stroke="#e8262d" stroke-width="1.3"/><ellipse cx="8" cy="8" rx="3" ry="6.5" fill="none" stroke="#e8262d" stroke-width="1.1"/><line x1="1.5" y1="8" x2="14.5" y2="8" stroke="#e8262d" stroke-width="1.1"/></svg>
          <span>www.yourdomain.com</span>
        </li>
        <li class="contact__item contact__item--address">
          <svg class="contact__icon" viewBox="0 0 16 16" aria-hidden="true"><path d="M8 15 C4 10 3 8 3 6 A5 5 0 0 1 13 6 C13 8 12 10 8 15 Z" fill="#e8262d"/><circle cx="8" cy="6" r="2" fill="#fff"/></svg>
          <span>P.O. Box 8321 Dunedin<br>New Zealand</span>
        </li>
      </ul>
    </div>
  </section>

</body>
</html>
```